Women's Health Company needs business card

We need a business card for a USA based women's health care company. We use digital technology to enhance therapy prescribed by clinicians for their patients

```html
<!DOCTYPE html>
<html lang="en">
<head>
<meta charset="utf-8">
<title>Lunera Health – Business Card</title>
<link rel="stylesheet" href="https://fonts.googleapis.com/css2?family=Roboto:wght@400;500;700&display=swap">
<style>
  :root {
    --stage: #2b2d31;
    --purple: #8f4fa8;
    --purple-light: #9a5cb3;
    --teal: #6cc6bd;
    --white: #ffffff;
    --ink-soft: #f1e9f5;
  }
  * { box-sizing: border-box; margin: 0; padding: 0; }
  html, body { width: 1200px; height: 900px; overflow: hidden; }
  body {
    background: var(--stage);
    font-family: "Roboto", Arial, sans-serif;
    display: flex;
    align-items: center;
    justify-content: center;
    gap: 60px;
  }
  .card {
    position: relative;
    width: 525px;
    height: 300px;
    border-radius: 4px;
    overflow: hidden;
    box-shadow: 0 14px 30px rgba(0,0,0,.45);
  }

  /* Front */
  .card--front { background: var(--white); }
  .card__wave { position: absolute; inset: 0; width: 100%; height: 100%; }
  .brand {
    position: absolute;
    display: flex;
    align-items: center;
    gap: 8px;
    font-weight: 400;
    color: var(--teal);
    letter-spacing: .5px;
  }
  .brand__dot {
    width: 9px; height: 9px;
    border-radius: 50%;
    background: var(--purple);
  }
  .card--front .brand { top: 34px; left: 36px; font-size: 30px; }

  .contact {
    position: absolute;
    left: 290px;
    top: 108px;
    color: var(--white);
  }
  .contact__name {
    font-size: 22px;
    font-weight: 700;
    color: var(--teal);
    line-height: 1.1;
  }
  .contact__role { font-size: 12px; font-weight: 500; margin-top: 3px; }
  .contact__address { font-size: 12px; line-height: 1.4; margin-top: 12px; }
  .contact__list { list-style: none; margin-top: 10px; font-size: 12px; line-height: 1.55; }
  .contact__list li { display: flex; align-items: center; gap: 6px; }
  .contact__icon { width: 10px; height: 10px; flex: none; }

  /* Back */
  .card--back {
    background: var(--purple);
    display: flex;
    align-items: center;
    justify-content: center;
  }
  .card__map {
    position: absolute;
    left: 60px; top: 40px;
    width: 405px; height: 220px;
    border-radius: 40px;
    background: radial-gradient(ellipse at center, rgba(255,255,255,.07), rgba(255,255,255,0) 70%);
  }
  .card--back .brand { position: relative; font-size: 38px; }
  .card--back .brand__dot { background: var(--white); width: 11px; height: 11px; }
</style>
</head>
<body>

  <section class="card card--front" aria-label="Business card front">
    <svg class="card__wave" viewBox="0 0 525 300" preserveAspectRatio="none" aria-hidden="true">
      <path d="M0,222 C150,215 280,60 525,64 L525,300 L0,300 Z" fill="#8f4fa8"/>
      <path d="M0,222 C150,215 280,60 525,64" fill="none" stroke="#6cc6bd" stroke-width="7"/>
    </svg>

    <div class="brand">
      <span class="brand__name">Lunera Health</span>
      <span class="brand__dot"></span>
    </div>

    <div class="contact">
      <h1 class="contact__name">Daniel Reyes</h1>
      <p class="contact__role">President and CEO</p>
      <p class="contact__address">48 Harbour Lane, Toronto<br>ON Canada M4B2K9</p>
      <ul class="contact__list">
        <li>
          <svg class="contact__icon" viewBox="0 0 10 10" aria-hidden="true"><path d="M2,1 L4,1 L4.6,3 L3.4,3.8 C4,5 5,6 6.2,6.6 L7,5.4 L9,6 L9,8 C5,8.5 1.5,5 2,1 Z" fill="#ffffff"/></svg>
          (+1) 555 014 2030
        </li>
        <li>
          <svg class="contact__icon" viewBox="0 0 10 10" aria-hidden="true"><rect x="1" y="2" width="8" height="6" fill="none" stroke="#ffffff" stroke-width="1"/><path d="M1,2 L5,5.5 L9,2" fill="none" stroke="#ffffff" stroke-width="1"/></svg>
          info@lunerahealth.com
        </li>
        <li>
          <svg class="contact__icon" viewBox="0 0 10 10" aria-hidden="true"><circle cx="5" cy="5" r="4" fill="none" stroke="#ffffff" stroke-width="1"/><path d="M1,5 H9 M5,1 C3,3.5 3,6.5 5,9 C7,6.5 7,3.5 5,1" fill="none" stroke="#ffffff" stroke-width=".8"/></svg>
          www.lunerahealth.com
        </li>
      </ul>
    </div>
  </section>

  <section class="card card--back" aria-label="Business card back">
    <div class="card__map" role="img" aria-label="Faint dotted world map"></div>
    <div class="brand">
      <span class="brand__name">Lunera Health</span>
      <span class="brand__dot"></span>
    </div>
  </section>

</body>
</html>
```